Email Sig, Letterhead, Business Card Design

Need a stationary package including email signature, letterhead/envelope, and business card design incorporating our new logo.

```html
<!DOCTYPE html>
<html lang="en">
<head>
<meta charset="utf-8">
<title>Marlow Engineering Stationery</title>
<link href="https://fonts.googleapis.com/css2?family=Inter:wght@400;600&display=swap" rel="stylesheet">
<style>
:root{
  --bg:#a9a7a8;
  --paper:#ffffff;
  --orange:#f05a28;
  --blue:#0c5f9e;
  --band:#e3e3e3;
  --ink:#3a3a3a;
  --dark:#1d1d1d;
}
*{margin:0;padding:0;box-sizing:border-box}
html,body{width:1200px;height:770px;overflow:hidden;background:var(--bg);font-family:"Inter",sans-serif}
.canvas{position:relative;width:1200px;height:770px}
.sheet{position:absolute;background:var(--paper)}
.frame{position:absolute;border:2px solid var(--blue)}
.brand{position:absolute;text-align:center;color:var(--orange);font-family:"Inter",sans-serif}
.brand-name{display:flex;align-items:center;justify-content:center;gap:5px;font-weight:600;font-size:13px;letter-spacing:.2px;color:var(--orange)}
.brand-dot{width:9px;height:9px;border-radius:50%;background:var(--orange)}
.brand-address{font-size:4.2px;color:var(--blue);font-weight:600;margin-top:2px}
.brand-reg{font-size:3.6px;letter-spacing:1px;color:var(--orange);margin-top:1px;display:flex;align-items:center;gap:3px;justify-content:center}
.brand-reg::before,.brand-reg::after{content:"";width:16px;height:.6px;background:var(--blue)}
.footer-band{position:absolute;left:0;right:0;top:570px;height:48px;background:var(--band)}
.footer-info{position:absolute;left:0;right:0;top:7px;text-align:center;font-size:10px;color:var(--dark);line-height:16px}
.footer-rule{width:385px;height:1.2px;background:var(--orange);margin:0 auto 1px}
.footer-contacts{display:flex;justify-content:center;gap:3px;align-items:center;white-space:nowrap}
.icon{width:7px;height:7px;vertical-align:-1px;fill:var(--blue)}
.letter{position:absolute;left:34px;top:221px;width:385px;color:var(--ink)}
.salutation{font-size:9.6px;margin-bottom:11px}
.letter p{font-size:6.6px;line-height:10.8px;text-align:justify;margin-bottom:10.8px}
.closing{font-size:7.2px;margin-top:30px}
.envelope{position:absolute;background:var(--paper)}
.envelope svg{position:absolute;left:0;top:0}
.flap-name{position:absolute;left:0;right:0;text-align:center;font-weight:600;font-size:8px}
</style>
</head>
<body>
<div class="canvas">

  <!-- Letterhead -->
  <section class="sheet letterhead" style="left:89px;top:66px;width:456px;height:642px">
    <div class="frame" style="left:7px;top:8px;width:440px;height:624px"></div>
    <div class="brand" style="left:0;right:0;top:91px">
      <div class="brand-name"><span class="brand-dot"></span>MARLOW ENGINEERING</div>
      <div class="brand-address">4120 CEDAR HOLLOW LANE, BROOKFIELD, TEXAS 77500</div>
      <div class="brand-reg">TBPE FIRM REGISTRATION F-4410</div>
    </div>
    <div class="letter">
      <div class="salutation">Dear Mr. Carter,</div>
      <p>Lorem ipsum dolor sit amet, consectetur adipiscing elit. Donec orci purus, luctus vitae dignissim eu, iaculis sed purus. Vivamus faucibus, ipsum nec aliquet viverra, leo mauris condimentum ligula, sit amet sagittis enim ligula quis arcu. Nam egestas tortor id nisi porttitor mattis. In tortor ante, ultricies in suscipit a, tempus non massa. Vivamus et auctor mi. Fusce vel massa nulla. Phasellus nec eros mauris, et scelerisque orci.</p>
      <p>Donec malesuada orci vitae nulla accumsan porta a id massa. Quisque accumsan iaculis magna sit amet fringilla. Maecenas consequat, magna eget tincidunt semper, odio nibh rutrum mi, id feugiat ante nisi eu risus. Vestibulum nunc orci, rhoncus a placerat in, ultricies in mi. Cras mattis varius eros, vel fringilla nisi suscipit eget. Quisque scelerisque sagittis nulla at porttitor.</p>
      <p>Sed id augue vitae urna euismod commodo aliquet a quam. Pellentesque arcu velit, cursus et malesuada ut, consequat et diam. Nullam erat sem, rhoncus id ullamcorper vitae, rhoncus et arcu. In ultricies ultricies nulla, ut rutrum nisi iaculis at. Donec eu magna a metus ornare faucibus. Fusce aliquet faucibus ultricies. Morbi semper, est id tincidunt gravida, sem arcu adipiscing lacus, ac bibendum nulla leo eu purus. Quisque nec diam sed risus consectetur accumsan quis quis nibh. Vestibulum id purus lorem.</p>
      <div class="closing">Sincerely,</div>
    </div>
    <div class="footer-band">
      <div class="footer-info">
        <div><svg class="icon" viewBox="0 0 10 10"><path d="M5 0a3.5 3.5 0 0 0-3.5 3.5C1.5 6 5 10 5 10s3.5-4 3.5-6.5A3.5 3.5 0 0 0 5 0zm0 5a1.5 1.5 0 1 1 0-3 1.5 1.5 0 0 1 0 3z"/></svg> Marlow Engineering 4120 Cedar Hollow Lane, Brookfield, Texas 77500</div>
        <div class="footer-rule"></div>
        <div class="footer-contacts">
          <svg class="icon" viewBox="0 0 10 10"><path d="M2 0l2 2.5-1 1.3a6 6 0 0 0 3.2 3.2l1.3-1L10 8 8.4 10C4 9.6.4 6 0 1.6z"/></svg>555-214-0187
          <svg class="icon" viewBox="0 0 10 10"><rect x="2" y="0" width="6" height="3"/><rect x="0" y="3.5" width="10" height="4"/><rect x="2" y="7" width="6" height="3"/></svg>555-214-0192
          <svg class="icon" viewBox="0 0 10 10"><path d="M0 2h10v6H0z"/><path d="M0 2l5 3.5L10 2" stroke="#fff" stroke-width=".8" fill="none"/></svg>info@marlowengineering.com
          <svg class="icon" viewBox="0 0 10 10"><circle cx="5" cy="5" r="5"/></svg>marlowengineering.com
        </div>
      </div>
    </div>
  </section>

  <!-- Back envelope -->
  <section class="envelope envelope-orange" style="left:629px;top:65px;width:509px;height:252px">
    <svg width="509" height="81" viewBox="0 0 509 81"><path d="M0 0H509L497 52Q491 81 462 81H47Q18 81 12 52Z" fill="var(--orange)"/></svg>
    <div class="flap-name" style="top:34px;color:var(--blue)">MARLOW ENGINEERING</div>
  </section>

  <!-- Front envelope -->
  <section class="envelope envelope-blue" style="left:579px;top:178px;width:509px;height:252px">
    <svg width="509" height="81" viewBox="0 0 509 81"><path d="M0 0H509L497 52Q491 81 462 81H47Q18 81 12 52Z" fill="var(--blue)"/></svg>
    <div class="flap-name" style="top:34px;color:var(--orange)">MARLOW ENGINEERING</div>
  </section>

  <!-- Compliment card -->
  <section class="sheet card" style="left:579px;top:458px;width:509px;height:250px">
    <div class="frame" style="left:11px;top:10px;width:488px;height:231px"></div>
    <div class="brand" style="left:25px;top:82px">
      <div class="brand-name"><span class="brand-dot"></span>MARLOW ENGINEERING</div>
      <div class="brand-address">4120 CEDAR HOLLOW LANE, BROOKFIELD, TEXAS 77500</div>
      <div class="brand-reg">TBPE FIRM REGISTRATION F-4410</div>
    </div>
    <div class="footer-band" style="top:178px">
      <div class="footer-info">
        <div><svg class="icon" viewBox="0 0 10 10"><path d="M5 0a3.5 3.5 0 0 0-3.5 3.5C1.5 6 5 10 5 10s3.5-4 3.5-6.5A3.5 3.5 0 0 0 5 0zm0 5a1.5 1.5 0 1 1 0-3 1.5 1.5 0 0 1 0 3z"/></svg> Marlow Engineering 4120 Cedar Hollow Lane, Brookfield, Texas 77500</div>
        <div class="footer-rule"></div>
        <div class="footer-contacts">
          <svg class="icon" viewBox="0 0 10 10"><path d="M2 0l2 2.5-1 1.3a6 6 0 0 0 3.2 3.2l1.3-1L10 8 8.4 10C4 9.6.4 6 0 1.6z"/></svg>555-214-0187
          <svg class="icon" viewBox="0 0 10 10"><rect x="2" y="0" width="6" height="3"/><rect x="0" y="3.5" width="10" height="4"/><rect x="2" y="7" width="6" height="3"/></svg>555-214-0192
          <svg class="icon" viewBox="0 0 10 10"><path d="M0 2h10v6H0z"/><path d="M0 2l5 3.5L10 2" stroke="#fff" stroke-width=".8" fill="none"/></svg>info@marlowengineering.com
          <svg class="icon" viewBox="0 0 10 10"><circle cx="5" cy="5" r="5"/></svg>marlowengineering.com
        </div>
      </div>
    </div>
  </section>

</div>
</body>
</html>
```